Supplement Bottle Packaging and Design

We want to rebrand our current health supplements (see below). We do want it to be modern, vibrant and appealing supplement bottles. Very upscale and elegant as it targets primarily women.
NOTE: READ THE ATTACHED WORD DOCUMENT!
Bottle size: We are totally open to the bottle size and shape, as long it's a typical supplement bottle size to handle 90-120 capsules; what we mostly need is new bottle design/packaging. YOU DON’T HAVE TO USE THE CURRENT WHITE BOTTLE SHAPE, BUT ANYTHING MORE MODERN WOULD WORK!
Updates
We need more modern, clean sleek designs to choose from
Look and feel
Each slider illustrates characteristics of the customer's brand and the style your logo design should communicate.

```html
<!DOCTYPE html>
<html lang="en">
<head>
<meta charset="utf-8">
<title>Bloom Formula Supplement Labels</title>
<link href="https://fonts.googleapis.com/css2?family=Poppins:wght@300;400;600;800&display=swap" rel="stylesheet">
<style>
  :root{
    --liver:#7a2fd0; --liver-light:#c08ae8;
    --tummy:#cf2222; --tummy-light:#ea7a7a;
    --hormone:#2b9a3c; --hormone-light:#86d08f;
    --sugar:#2430d4; --sugar-light:#6f86ea;
    --paper:#ffffff; --ink:#333340; --bg:#ffffff;
  }
  *{box-sizing:border-box;margin:0;padding:0}
  html,body{width:1200px;height:652px;overflow:hidden;background:var(--bg)}
  body{font-family:'Poppins',sans-serif;position:relative}
  .range{position:absolute;left:50px;top:70px;display:flex;gap:40px}
  .label{width:245px;height:520px;border-radius:22px;overflow:hidden;background:var(--paper);
    box-shadow:0 6px 24px rgba(0,0,0,.12);display:flex;flex-direction:column;color:var(--c)}
  .label.liver{--c:var(--liver);--l:var(--liver-light)}
  .label.tummy{--c:var(--tummy);--l:var(--tummy-light)}
  .label.hormone{--c:var(--hormone);--l:var(--hormone-light)}
  .label.sugar{--c:var(--sugar);--l:var(--sugar-light)}
  .cap{height:34px;background:var(--c);filter:brightness(.85);
    background-image:repeating-linear-gradient(90deg,rgba(255,255,255,.18) 0 2px,transparent 2px 6px)}
  .face{height:344px;background:linear-gradient(115deg,var(--c) 45%,var(--l));padding:0 18px;
    display:flex;flex-direction:column;justify-content:flex-end;padding-bottom:18px;color:#fff}
  .name{font-weight:800;line-height:.95;text-transform:uppercase}
  .bloom{font-weight:800;font-size:62px;line-height:1;letter-spacing:-1px}
  .formula{font-weight:300;font-size:20px;letter-spacing:17px;opacity:.55;margin-top:6px}
  .tagline{background:var(--paper);color:var(--c);font-weight:600;font-size:10.5px;
    text-align:center;padding:8px 4px;margin:0 12px;border-radius:4px 4px 0 0;white-space:nowrap}
  .benefits{background:var(--c);margin:0 12px;display:flex;justify-content:space-between;
    padding:8px 6px;border-radius:0 0 6px 6px;color:#fff}
  .benefit{display:flex;align-items:center;gap:4px;font-size:7px;line-height:1.25;opacity:.95}
  .benefit svg{width:12px;height:12px;flex:none}
  .base{padding:22px 0 0 34px;border-left:0}
  .base-inner{border-left:1.5px solid var(--c);padding-left:8px}
  .kind{font-weight:300;font-size:16px;line-height:1.1}
  .count{font-size:10px;color:var(--ink);margin-top:4px}
</style>
</head>
<body>
<main class="range">
  <section class="label liver">
    <div class="cap"></div>
    <div class="face">
      <div class="name" style="font-size:66px">Liver</div>
      <div class="bloom">Bloom</div>
      <div class="formula">FORMULA</div>
    </div>
    <div class="tagline">Rejuvenating Cleanse &amp; Detox Formula</div>
    <div class="benefits">
      <div class="benefit"><svg viewBox="0 0 12 12"><circle cx="6" cy="6" r="5" fill="none" stroke="#fff"/><path d="M3.5 6l2 2 3-4" fill="none" stroke="#fff"/></svg>Supports<br>Liver Health</div>
      <div class="benefit"><svg viewBox="0 0 12 12"><circle cx="6" cy="6" r="5" fill="none" stroke="#fff"/><path d="M3.5 6l2 2 3-4" fill="none" stroke="#fff"/></svg>Promotes Liver<br>Detoxification</div>
      <div class="benefit"><svg viewBox="0 0 12 12"><circle cx="6" cy="6" r="5" fill="none" stroke="#fff"/><path d="M3.5 6l2 2 3-4" fill="none" stroke="#fff"/></svg>Antioxidant<br>Support</div>
    </div>
    <div class="base"><div class="base-inner"><div class="kind">Dietary Supplement</div><div class="count">120 Vegetable Capsules</div></div></div>
  </section>

  <section class="label tummy">
    <div class="cap"></div>
    <div class="face">
      <div class="name" style="font-size:52px">Tummy</div>
      <div class="bloom">Bloom</div>
      <div class="formula">FORMULA</div>
    </div>
    <div class="tagline">Oxygenating Colon Cleanse</div>
    <div class="benefits">
      <div class="benefit"><svg viewBox="0 0 12 12"><circle cx="6" cy="6" r="5" fill="none" stroke="#fff"/><path d="M3.5 6l2 2 3-4" fill="none" stroke="#fff"/></svg>Cleanses the<br>digestive tract</div>
      <div class="benefit"><svg viewBox="0 0 12 12"><circle cx="6" cy="6" r="5" fill="none" stroke="#fff"/><path d="M3.5 6l2 2 3-4" fill="none" stroke="#fff"/></svg>Supports<br>regularity</div>
      <div class="benefit"><svg viewBox="0 0 12 12"><circle cx="6" cy="6" r="5" fill="none" stroke="#fff"/><path d="M3.5 6l2 2 3-4" fill="none" stroke="#fff"/></svg>Supports<br>Gut Health</div>
    </div>
    <div class="base"><div class="base-inner"><div class="kind">Dietary Supplement</div><div class="count">90 Vegetable Capsules</div></div></div>
  </section>

  <section class="label hormone">
    <div class="cap"></div>
    <div class="face">
      <div class="name" style="font-size:38px">Hormone</div>
      <div class="bloom">Bloom</div>
      <div class="formula">FORMULA</div>
    </div>
    <div class="tagline">Supports Healthy Hormone Levels</div>
    <div class="benefits">
      <div class="benefit"><svg viewBox="0 0 12 12"><circle cx="6" cy="6" r="5" fill="none" stroke="#fff"/><path d="M3.5 6l2 2 3-4" fill="none" stroke="#fff"/></svg>Balances<br>Estrogen</div>
      <div class="benefit"><svg viewBox="0 0 12 12"><circle cx="6" cy="6" r="5" fill="none" stroke="#fff"/><path d="M3.5 6l2 2 3-4" fill="none" stroke="#fff"/></svg>Hormone<br>Balance</div>
      <div class="benefit"><svg viewBox="0 0 12 12"><circle cx="6" cy="6" r="5" fill="none" stroke="#fff"/><path d="M3.5 6l2 2 3-4" fill="none" stroke="#fff"/></svg>Balances<br>Body Fat</div>
    </div>
    <div class="base"><div class="base-inner"><div class="kind">Dietary Supplement</div><div class="count">60 Vegetable Capsules</div></div></div>
  </section>

  <section class="label sugar">
    <div class="cap"></div>
    <div class="face">
      <div class="name" style="font-size:28px">Blood Sugar</div>
      <div class="bloom">Bloom</div>
      <div class="formula">FORMULA</div>
    </div>
    <div class="tagline">Supports Healthy Blood Glucose Levels</div>
    <div class="benefits">
      <div class="benefit"><svg viewBox="0 0 12 12"><circle cx="6" cy="6" r="5" fill="none" stroke="#fff"/><path d="M3.5 6l2 2 3-4" fill="none" stroke="#fff"/></svg>Sugar &amp; Carb<br>Balance</div>
      <div class="benefit"><svg viewBox="0 0 12 12"><circle cx="6" cy="6" r="5" fill="none" stroke="#fff"/><path d="M3.5 6l2 2 3-4" fill="none" stroke="#fff"/></svg>Insulin<br>Balance</div>
      <div class="benefit"><svg viewBox="0 0 12 12"><circle cx="6" cy="6" r="5" fill="none" stroke="#fff"/><path d="M3.5 6l2 2 3-4" fill="none" stroke="#fff"/></svg>Supports<br>Inflammation</div>
    </div>
    <div class="base"><div class="base-inner"><div class="kind">Dietary Supplement</div><div class="count">60 Vegetable Capsules</div></div></div>
  </section>
</main>
</body>
</html>
```